Mirela Dawn Business Card Design

I need a business card for my daughter. She has it all described in the file below. But it needs to be square in shape. http://www.mireladawn.example is her web site

Target Market(s)

18-35 year old women

Industry/Entity Type

Fashion

Contact Information for Business Card

Please look at the attached file as it has all the details.

Requirements
Must have
• Please look at the attached file as it has all the details.
Nice to have
Should not have

```html
<!DOCTYPE html>
<html lang="en">
<head>
<meta charset="utf-8">
<title>Mirela Dawn Business Card</title>
<link rel="stylesheet" href="https://fonts.googleapis.com/css2?family=Cormorant+Garamond:wght@500;700&family=Dancing+Script:wght@500&display=swap">
<style>
  :root {
    --page: #ebebeb;
    --ink: #0b0b0b;
    --blush: #fbdbe3;
    --marble-dark: #121212;
    --marble-mid: #3a3a3a;
    --white: #ffffff;
  }
  * { box-sizing: border-box; margin: 0; padding: 0; }
  html, body { width: 1200px; height: 1000px; overflow: hidden; }
  body { background: var(--page); position: relative; font-family: "Cormorant Garamond", serif; color: var(--ink); }

  .card { position: absolute; width: 490px; height: 490px; top: 255px; }
  .card--front { left: 81px; }
  .card--back { left: 630px; background: var(--ink); }

  .marble {
    position: absolute; inset: 0;
    background: radial-gradient(circle at 30% 40%, var(--marble-mid), var(--marble-dark) 60%),
                linear-gradient(135deg, var(--marble-dark), var(--marble-mid), var(--marble-dark));
    background-blend-mode: screen;
  }
  .front-panel {
    position: absolute; left: 57px; top: 58px; width: 376px; height: 374px;
    background: var(--blush);
    display: flex; align-items: center; justify-content: center;
  }
  .brand-name {
    font-family: "Cormorant Garamond", serif; font-weight: 700;
    font-size: 52px; line-height: 1; letter-spacing: 3px;
    text-align: center; color: var(--ink);
  }

  .back-title {
    position: absolute; top: 14px; width: 100%; text-align: center;
    color: var(--white); font-family: "Cormorant Garamond", serif; font-weight: 700;
    font-size: 24px; letter-spacing: 1px;
  }
  .contact-panel {
    position: absolute; left: 51px; top: 52px; width: 388px; height: 385px;
    background: var(--blush); padding: 20px 0 0 20px;
  }
  .contact-list { list-style: none; }
  .contact-item { display: flex; align-items: center; height: 60.4px; }
  .contact-icon {
    width: 38px; height: 38px; border-radius: 50%; background: var(--ink);
    flex: none; display: flex; align-items: center; justify-content: center;
  }
  .contact-text { margin-left: 14px; font-size: 23px; font-weight: 500; white-space: nowrap; }
  .back-footer {
    position: absolute; bottom: 14px; width: 100%; text-align: center;
    color: var(--white); font-family: "Dancing Script", cursive; font-size: 18px;
  }
</style>
</head>
<body>
  <section class="card card--front">
    <div class="marble" role="img" aria-label="Black marble texture with white veins"></div>
    <div class="front-panel">
      <h1 class="brand-name">MIRELA DAWN</h1>
    </div>
  </section>

  <section class="card card--back">
    <h2 class="back-title">MIRELA DAWN</h2>
    <div class="contact-panel">
      <ul class="contact-list">
        <li class="contact-item"><span class="contact-icon"></span><span class="contact-text">pixgram.example/mireladawnxo</span></li>
        <li class="contact-item"><span class="contact-icon"></span><span class="contact-text">chirpline.example/mireladawnxo</span></li>
        <li class="contact-item"><span class="contact-icon"></span><span class="contact-text">@mireladawnxo</span></li>
        <li class="contact-item"><span class="contact-icon">
          <svg width="20" height="14" viewBox="0 0 20 14"><rect x="1" y="1" width="18" height="12" fill="none" stroke="#fff" stroke-width="1.8"/><path d="M1 1 L10 8 L19 1" fill="none" stroke="#fff" stroke-width="1.8"/></svg>
        </span><span class="contact-text">mirela@mireladawn.example</span></li>
        <li class="contact-item"><span class="contact-icon"></span><span class="contact-text">mireladawn.example</span></li>
        <li class="contact-item"><span class="contact-icon"></span><span class="contact-text">vidstream.example/mireladawn</span></li>
      </ul>
    </div>
    <p class="back-footer">blogger &amp; creator // beauty - fashion - travel</p>
  </section>
</body>
</html>
```